Verdane Kiwi Root Essence Prime Serum - Product Label

Hi Guys,

I threw up a rough label sketch. Looking to keep the label clean and fresh.

LABEL DIMENSIONS: 4.05 in (Height) x 1.18 in (Diameter)

Industry/Entity Type

Beauty Aid

Font styles to use
Serif

Colors
0255a3
0592cd
6b449b
ffc214

Requirements
Must have
• Lumivelle
• __________
• S K I N
Nice to have
• We can try purple, gold and black or stick with the blue scheme we have going.

```html
<!DOCTYPE html>
<html lang="en">
<head>
<meta charset="utf-8">
<title>Verdane Kiwi Root Essence Prime Serum – Label</title>
<link rel="stylesheet" href="https://fonts.googleapis.com/css2?family=Cinzel:wght@400;500&family=Open+Sans:wght@400;600;700&family=Catamaran:wght@400;500;600&family=Tinos:wght@400;700&display=swap">
<style>
  :root {
    --brand-deep: #0255a3;
    --brand-sky: #0592cd;
    --brand-aqua: #4fb6dc;
    --ink: #2a4f86;
    --text-body: #2e5a8c;
    --paper: #ffffff;
    --volume-ink: #1f2e45;
    --badge-pink: #f07ab1;
    --badge-grey: #6e6e6e;
    --badge-green: #3f9b3a;
  }
  * { box-sizing: border-box; margin: 0; padding: 0; }
  html, body { width: 1060px; height: 1200px; overflow: hidden; background: var(--paper); }
  .canvas { position: relative; width: 1060px; height: 1200px; background: var(--paper); }

  .label {
    position: absolute; left: 30px; top: 380px;
    width: 1000px; height: 440px;
    border-radius: 6px; overflow: hidden;
    background: var(--paper);
  }
  .label__art { position: absolute; inset: 0; width: 100%; height: 100%; }

  .ingredients {
    position: absolute; left: 25px; top: 68px; width: 250px;
    font-family: "Open Sans", sans-serif; font-size: 15.5px; line-height: 19.5px;
    color: var(--text-body); text-align: justify; letter-spacing: -0.3px;
  }
  .ingredients strong { font-weight: 700; }
  .directions { margin-top: 20px; }

  .front {
    position: absolute; left: 320px; width: 360px; top: 0; text-align: center;
  }
  .brand {
    margin-top: 100px;
    font-family: "Cinzel", serif; font-size: 38px; font-weight: 400;
    letter-spacing: 2px; color: var(--brand-sky);
  }
  .product-name {
    margin-top: 38px;
    font-family: "Catamaran", sans-serif; font-weight: 500;
    font-size: 38px; line-height: 40px; color: var(--ink); letter-spacing: -0.5px;
  }
  .product-name .accent { color: var(--brand-aqua); }
  .product-type {
    margin-top: 4px;
    font-family: "Tinos", serif; font-size: 21px; font-weight: 700;
    letter-spacing: 14px; color: var(--ink); padding-left: 14px;
  }
  .volume {
    margin-top: 12px;
    font-family: "Tinos", serif; font-size: 22px; color: var(--volume-ink);
  }

  .side-brand {
    position: absolute; left: 740px; top: 40px;
    font-family: "Cinzel", serif; font-size: 28px; letter-spacing: 1px; color: var(--paper);
  }
  .distributor {
    position: absolute; left: 740px; top: 120px;
    font-family: "Catamaran", sans-serif; font-size: 17px; line-height: 26px; color: var(--ink);
  }
  .distributor strong { font-weight: 600; }
  .badges { position: absolute; left: 750px; top: 222px; display: flex; gap: 24px; align-items: center; }
  .badge--pink { background: var(--badge-pink); border-radius: 50%; width: 46px; height: 46px; }
  .badge--square { border: 2px solid var(--badge-grey); background: var(--paper); width: 44px; height: 40px; border-radius: 4px; }
  .badge--green { background: var(--badge-green); border-radius: 50%; width: 68px; height: 68px; }
</style>
</head>
<body>
<main class="canvas">
  <section class="label">
    <svg class="label__art" viewBox="0 0 1000 440" preserveAspectRatio="none" aria-hidden="true">
      <defs>
        <linearGradient id="band" x1="0" y1="0" x2="1" y2="0">
          <stop offset="0" stop-color="#0a6fbf"/>
          <stop offset="0.5" stop-color="#0592cd"/>
          <stop offset="1" stop-color="#0255a3"/>
        </linearGradient>
      </defs>
      <path d="M0,0 H1000 V110 C880,90 760,70 640,64 L500,88 L360,62 C230,56 110,50 0,44 Z" fill="url(#band)"/>
    </svg>
    <svg class="label__art" viewBox="0 0 1000 440" preserveAspectRatio="none" role="img" aria-label="Soft flowing blue wave pattern across the lower part of the label">
      <defs>
        <linearGradient id="swirl" x1="0" y1="0" x2="0" y2="1">
          <stop offset="0" stop-color="#ffffff" stop-opacity="0"/>
          <stop offset="0.45" stop-color="#cfe5f7"/>
          <stop offset="1" stop-color="#8ec3ec"/>
        </linearGradient>
      </defs>
      <path d="M0,250 C200,210 380,300 520,270 C680,235 820,200 1000,230 V440 H0 Z" fill="url(#swirl)"/>
    </svg>

    <div class="ingredients">
      <p><strong>Ingredient List:</strong> Purified Water, (BotaniCellTec Stem Cell) Actinidia Chinensis, Glycerin, Lecithin, Phenoxyethanol Collagen, Palmitoyl Tetrapeptide-3, Peptilux 3000), Propylene Glycol, Polyglutamic Acid, Phenoxyethanol, Hydroxyethylcellulose, Propylene Glycol, Benzylalcohol, Dehydroacetic Acid</p>
      <p class="directions">How to use: Wash area where you will apply the Verdane Kiwi Root Serum thoroughly. Apply the product and let absorb for 15 minutes then apply moisturizer if desired.</p>
    </div>

    <div class="front">
      <div class="brand">Lumivelle</div>
      <h1 class="product-name">VERDANE <span class="accent">KIWI</span> ROOT<br>ESSENCE <span class="accent">PRIME</span></h1>
      <div class="product-type">SKIN</div>
      <div class="volume">1fl. oz/30ml</div>
    </div>

    <div class="side-brand">Lumivelle</div>
    <div class="distributor">
      <p><strong>Distributed by</strong> Lumivelle</p>
      <p>Address</p>
      <p>website</p>
    </div>
    <div class="badges">
      <div class="badge--pink" role="img" aria-label="Cruelty free badge"></div>
      <div class="badge--square" role="img" aria-label="Period after opening badge"></div>
      <div class="badge--green" role="img" aria-label="Manufacturing practice badge"></div>
    </div>
  </section>
</main>
</body>
</html>
```